Online trading school - Website design

We are building an online trading school (trading of shares, commodities, indices, currencies). The purpose is to teach online traders how to trade successfully. We need to design the homepage of the website and logo (plumeridge.com will be the domain). The homepage will contain the following elements

- logo
- Sign in and Register links/buttons
- upper menu
- short introduction
- a couple of bullet points 'Why to join our school?'
- sign up form
- text
- bottom menu

Attached is a draft for the designer. The draft is just for an inspiration, the actual structure of the website can be different if the designer thinks so.

The designer is free to choose colors.

School

3 page

```html
<!DOCTYPE html>
<html lang="en">
<head>
<meta charset="utf-8">
<title>Plumeridge – Online Trading School</title>
<link href="https://fonts.googleapis.com/css2?family=Arimo:wght@400;700&display=swap" rel="stylesheet">
<style>
:root{
  --orange:#e05a0a;
  --blue:#3461a0;
  --navy-text:#2e5a96;
  --dark:#3d3d3d;
  --btn-dark:#333a44;
  --panel:#efefef;
  --ink:#3a3a3a;
  --white:#fff;
}
*{box-sizing:border-box;margin:0;padding:0}
html,body{width:1040px;height:1200px;overflow:hidden}
body{font-family:Arimo,Helvetica,Arial,sans-serif;color:var(--ink);background:var(--white);position:relative}
.site-header{height:74px;position:relative}
.brand{position:absolute;left:40px;top:22px;display:flex;align-items:center;gap:8px}
.brand-mark{width:24px;height:24px;background:var(--orange)}
.brand-name{font-size:28px;font-weight:700;color:var(--navy-text);letter-spacing:-.3px}
.social{position:absolute;left:710px;top:26px;display:flex;gap:9px}
.social span{width:23px;height:23px;border:1.5px solid #444;border-radius:50%}
.auth{position:absolute;right:40px;top:23px;display:flex;gap:9px}
.auth a{display:block;height:29px;line-height:29px;padding:0 8px;color:var(--white);font-size:12.5px;text-decoration:none;border-radius:2px}
.auth .sign-in{background:var(--btn-dark);padding:0 13px}
.auth .register{background:var(--navy-text)}
.main-nav{height:40px;background:var(--orange);display:flex;padding-left:66px}
.main-nav a{color:var(--white);text-decoration:none;font-size:13px;line-height:40px;padding:0 6px;margin-right:50px;position:relative}
.main-nav a.active::after{content:"";position:absolute;left:0;right:0;bottom:0;height:3px;background:#2b2b2b}
.main-nav a.active{padding:0 8px 0 6px;margin-right:48px}
.hero{height:316px;background:linear-gradient(180deg,#3565a6,#3160a0);text-align:center;padding-top:56px}
.hero h1{color:var(--white);font-weight:400;font-size:30px;line-height:48px;letter-spacing:.3px;width:860px;margin:0 auto}
.hero .cta{display:inline-flex;align-items:center;gap:8px;margin-top:26px;background:var(--orange);color:var(--white);font-size:15px;height:40px;padding:0 22px 0 15px;border-radius:3px;text-decoration:none}
.why{position:absolute;left:45px;top:490px;width:420px}
.why h2{font-size:24px;font-weight:700;letter-spacing:.5px}
.why .rule{width:93px;height:2px;background:#aaa;margin:12px 0 14px}
.why li{list-style:none;display:flex;align-items:center;gap:12px;font-size:17px;letter-spacing:.5px;height:48px;margin-top:-10px;margin-bottom:10px}
.join{position:absolute;left:586px;top:474px;width:414px;height:308px;background:var(--panel);padding:16px 23px}
.join h2{font-size:24px;font-weight:700;letter-spacing:.5px;margin-bottom:22px}
.join .field{display:block;width:367px;height:34px;background:var(--white);border:0;margin-bottom:12px;font:13px Arimo,sans-serif;color:#666;padding:0 11px;line-height:34px}
.join .agree{display:flex;align-items:center;gap:9px;font-size:13px;margin:20px 0 0 7px}
.join .box{width:15px;height:15px;border:1.5px solid #bbb;background:var(--white)}
.join .submit{position:absolute;right:24px;bottom:28px;width:87px;height:34px;background:var(--orange);color:var(--white);font-weight:700;font-size:13px;text-align:center;line-height:34px}
.offer{position:absolute;left:0;top:830px;width:1040px;height:324px;background:var(--panel);text-align:center;padding-top:22px}
.offer h2{font-weight:400;font-size:25px;letter-spacing:.5px}
.offer .rule{width:92px;height:2px;background:#aaa;margin:14px auto 22px}
.offer p{font-size:13.5px;line-height:19.2px;width:910px;margin:0 auto 19px}
.site-footer{position:absolute;left:0;top:1154px;width:1040px;height:46px;background:var(--dark);color:var(--white);font-size:13.5px;display:flex;justify-content:space-between;align-items:center;padding:0 40px}
</style>
</head>
<body>
<header class="site-header">
  <div class="brand"><span class="brand-mark"></span><span class="brand-name">PLUMERIDGE.COM</span></div>
  <div class="social" aria-label="Social links"><span></span><span></span><span></span><span></span></div>
  <nav class="auth"><a class="sign-in" href="#">SIGN IN</a><a class="register" href="#">REGISTER</a></nav>
</header>
<nav class="main-nav">
  <a class="active" href="#">ABOUT OUR SCHOOL</a>
  <a href="#">RISK WARNING</a>
  <a href="#">FAQ</a>
  <a href="#">TRADING GLOSSARY</a>
  <a href="#">CONTACT</a>
</nav>
<section class="hero" role="img" aria-label="Blue-tinted trading chart background">
  <h1>AN ONLINE DIGITAL TRADING COURSE THAT WILL WALK YOU THROUGH THE SIMPLE PROCESS OF EXTRACTING CASH FROM THE MARKET</h1>
  <a class="cta" href="#"><svg width="20" height="20" viewBox="0 0 20 20"><circle cx="10" cy="10" r="8.8" fill="none" stroke="#fff" stroke-width="1.4"/><circle cx="6.5" cy="10" r="1.1" fill="#fff"/><circle cx="10" cy="10" r="1.1" fill="#fff"/><circle cx="13.5" cy="10" r="1.1" fill="#fff"/></svg>LEARN MORE</a>
</section>
<section class="why">
  <h2>WHY TO JOIN US?</h2>
  <div class="rule"></div>
  <ul>
    <li><svg width="15" height="14" viewBox="0 0 15 14"><path d="M1 7h10M7 2l5 5-5 5" fill="none" stroke="#e05a0a" stroke-width="3"/></svg>Best trading tips ever</li>
    <li><svg width="15" height="14" viewBox="0 0 15 14"><path d="M1 7h10M7 2l5 5-5 5" fill="none" stroke="#e05a0a" stroke-width="3"/></svg>Secret tips from experts</li>
    <li><svg width="15" height="14" viewBox="0 0 15 14"><path d="M1 7h10M7 2l5 5-5 5" fill="none" stroke="#e05a0a" stroke-width="3"/></svg>We teach you how to trade online</li>
    <li><svg width="15" height="14" viewBox="0 0 15 14"><path d="M1 7h10M7 2l5 5-5 5" fill="none" stroke="#e05a0a" stroke-width="3"/></svg>Learn how to trade commodities</li>
    <li><svg width="15" height="14" viewBox="0 0 15 14"><path d="M1 7h10M7 2l5 5-5 5" fill="none" stroke="#e05a0a" stroke-width="3"/></svg>Learn How to become a trader</li>
  </ul>
</section>
<section class="join">
  <h2>JOIN OUR SCHOOL NOW!</h2>
  <div class="field">First name</div>
  <div class="field">Last name</div>
  <div class="field">Email</div>
  <div class="agree"><span class="box"></span>Agree with our terms and conditions</div>
  <div class="submit">SUBMIT</div>
</section>
<section class="offer">
  <h2>WHAT DO WE OFFER?</h2>
  <div class="rule"></div>
  <p>Lorem Ipsum is simply dummy text of the printing and typesetting industry. Lorem Ipsum has been the industry's standard dummy text ever since the 1500s, when an unknown printer took a galley of type and scrambled it to make a type specimen book. It has survived not only five centuries, but also the leap into electronic typesetting, remaining essentially unchanged. It was popularised in the 1960s with the release of Typerow sheets containing Lorem Ipsum passages, and more recently with desktop publishing software like Quillset Layout including versions of Lorem Ipsum.</p>
  <p>Lorem Ipsum is simply dummy text of the printing and typesetting industry. Lorem Ipsum has been the industry's standard dummy text ever since the 1500s, when an unknown printer took a galley of type and scrambled it to make a type specimen book. It has survived not only five centuries, but also the leap into electronic typesetting, remaining essentially unchanged.</p>
</section>
<footer class="site-footer">
  <span>Copyright © Plumeridge.com. All Rights Reserved.</span>
  <span>Terms &amp; Conditions &nbsp;|&nbsp; Privacy Policy</span>
</footer>
</body>
</html>
```